One Page Website for Personal Trainer in London

I have a logo and need a one page website designed around my branding. I am a freelance Personal Trainer based in London specialising in bodyweight training for men and women. I would like the site to be modern and clean but not overtly urban in design.
I need the following headings:
About Me
My Services
Events
Blog
I don't need them to be seperate pages but if they can link to further down the page that would be great.
Industry/Entity Type
Personal Trainer
Coding
Coded - Design and coding required
Number of Pages Required
1 page
Requirements
Must have
- I need the following headings:
- About Me
- My Services
- Events
- Blog
- mobile friendly formatting
- health and fitness related photography
- Colour scheme in keeping with my existing logo

```html
<!DOCTYPE html>
<html lang="en">
<head>
<meta charset="utf-8">
<title>Marlowe Finch – Personal Training</title>
<link href="https://fonts.googleapis.com/css2?family=Montserrat:wght@400;600;700&family=Open+Sans:ital,wght@0,400;0,600;0,700;1,600&display=swap" rel="stylesheet">
<style>
:root{
  --orange:#f7941d;
  --orange-soft:#fde3c4;
  --cream:#fdf0e0;
  --dark:#262626;
  --ink:#1e1e1e;
  --muted:#6d6d6d;
  --white:#ffffff;
  --grey-bg:#d9dadc;
}
*{box-sizing:border-box;margin:0;padding:0}
html,body{width:1200px;height:4369px;overflow:hidden}
body{font-family:"Open Sans",Arial,sans-serif;color:var(--ink);background:var(--white);position:relative}
section,header,footer{position:absolute;left:0;width:1200px}
.abs{position:absolute}
.btn{position:absolute;background:var(--orange);color:var(--white);font-weight:700;text-transform:uppercase;display:flex;align-items:center;justify-content:center;font-family:"Open Sans",Arial,sans-serif}
.photo{position:absolute}

/* header */
.site-header{top:0;height:183px;background:var(--white)}
.brand{left:82px;top:50px;display:flex;align-items:center;gap:16px}
.brand-dot{width:46px;height:46px;border-radius:50%;background:var(--orange)}
.brand-name{font-family:"Montserrat",sans-serif;font-size:34px;font-weight:600;color:var(--ink)}
.contact{top:40px;right:56px;display:flex;gap:40px;font-size:20px;font-weight:600}
.contact span{display:flex;align-items:center;gap:12px}
.main-nav{left:568px;top:99px;width:632px;height:38px;background:var(--dark);display:flex;align-items:center;padding-left:110px}
.nav-ring{position:absolute;left:-2px;top:-20px;width:50px;height:50px;border-radius:50%;border:8px solid var(--orange);background:var(--white)}
.main-nav a{color:var(--white);font-size:14px;text-decoration:none;padding:0 20px;border-right:1px solid #555}
.main-nav a:last-child{border:none}
.main-nav a.active{color:var(--orange)}

/* hero */
.hero{top:183px;height:816px;background:linear-gradient(90deg,#b9b5b1 0%,#d8d8da 45%,#e4e4e6 100%)}
.hero-photo{left:0;top:0;width:640px;height:816px;background:radial-gradient(ellipse at 45% 45%,#8a6b55 0%,#5c4535 40%,rgba(180,176,172,0) 75%)}
.hero-kicker{right:84px;top:340px;font-size:46px;color:var(--ink)}
.hero-title{right:80px;top:395px;text-align:right;font-size:88px;font-weight:700;line-height:1;color:var(--ink)}
.hero-sub{right:84px;top:565px;font-size:30px}
.hero .btn{left:827px;top:667px;width:292px;height:56px;font-size:24px;text-transform:none}

/* about */
.about{top:999px;height:478px}
.section-title{font-family:"Open Sans",sans-serif;font-weight:700;font-size:44px}
.about .section-title{left:96px;top:68px}
.about-lead{left:96px;top:157px;width:420px;font-size:14px;font-weight:700;text-transform:uppercase;line-height:1.35}
.about-text{left:96px;top:225px;width:420px;font-size:12px;color:var(--muted);line-height:1.6}
.about .btn{left:96px;top:365px;width:164px;height:36px;font-size:11px}
.about-photo{left:612px;top:20px;width:509px;height:460px;background:radial-gradient(ellipse at 50% 45%,#c79c80 0%,#6b5d66 45%,rgba(255,255,255,0) 72%)}

/* band */
.band{top:1477px;height:804px;background:linear-gradient(90deg,#f5cfa2 0%,var(--orange-soft) 50%,#f7d5ad 100%)}
.band-photo{left:0;top:0;width:1200px;height:804px;background:radial-gradient(ellipse at 22% 55%,rgba(90,70,55,.55) 0%,rgba(0,0,0,0) 35%),radial-gradient(ellipse at 80% 60%,rgba(90,70,55,.5) 0%,rgba(0,0,0,0) 35%)}
.band-lead{left:0;width:1200px;top:493px;text-align:center;font-size:31px;font-style:italic;font-weight:600}
.band-title{left:0;width:1200px;top:535px;text-align:center;font-family:"Montserrat",sans-serif;font-size:78px;line-height:1.18;color:var(--orange);text-transform:uppercase;font-weight:400}

/* services */
.services{top:2281px;height:623px}
.services .section-title{left:0;width:1200px;text-align:center;top:60px}
.service-card{top:175px;width:280px;height:291px;background:var(--orange);border:4px solid var(--orange)}
.service-img{width:272px;height:176px}
.service-name{text-align:center;color:var(--white);font-weight:700;font-size:19px;margin-top:14px}
.service-text{text-align:center;color:var(--white);font-size:12px;line-height:1.4;padding:6px 22px 0}
.services .btn{left:524px;top:527px;width:163px;height:33px;font-size:11px}

/* blog */
.blog{top:2904px;height:734px;background:var(--orange)}
.blog .section-title{left:0;width:1200px;text-align:center;top:40px;color:var(--white)}
.post{left:96px;width:1011px;height:140px;background:var(--cream);display:flex}
.post-img{width:198px;height:140px;position:relative}
.post-date{position:absolute;left:0;top:0;width:30px;height:30px;background:var(--orange);color:var(--white);font-size:10px;font-weight:700;display:flex;align-items:center;justify-content:center}
.post-body{padding:22px 28px 0 34px;width:813px}
.post-title{font-size:17px;font-weight:600;margin-bottom:16px}
.post-text{font-size:11.5px;line-height:1.45;color:#444}
.blog .btn{left:518px;top:664px;width:164px;height:38px;font-size:11px;background:var(--white);color:var(--ink)}

/* events & testimonials */
.lower{top:3638px;height:426px}
.col-title{top:68px;font-size:30px;font-weight:700;color:var(--orange)}
.arrows{top:74px;display:flex;gap:6px}
.arrows span{width:22px;height:22px;border-radius:50%;background:var(--orange);display:flex;align-items:center;justify-content:center}
.rule{top:118px;height:2px;background:#e0e0e0}
.event{left:96px;width:460px;display:flex;gap:34px}
.event-date{width:58px}
.event-day{height:48px;background:var(--dark);color:var(--white);font-size:22px;font-weight:700;display:flex;align-items:center;justify-content:center}
.event-month{height:24px;background:var(--orange);color:var(--white);font-size:12px;display:flex;align-items:center;justify-content:center}
.event-title{font-size:16px;font-weight:600;margin:6px 0 12px}
.event-text{font-size:12px;color:#555;line-height:1.5}
.event-sep{left:96px;width:460px;height:1px;background:#ddd}
.avatar{left:690px;top:145px;width:110px;height:110px;border-radius:50%;background:linear-gradient(160deg,#e8c9b4,#b78d77)}
.avatar-name{left:690px;top:268px;width:110px;text-align:center;font-size:11px;color:var(--orange);font-weight:700;text-transform:uppercase}
.quote{left:822px;top:145px;width:290px;font-size:12.5px;line-height:1.55;color:#444}
.quote b{color:var(--orange);font-size:18px}

/* footer */
.site-footer{top:4064px;height:253px;background:var(--dark);color:var(--white);text-align:center}
.address{position:absolute;left:0;width:1200px;top:62px;font-size:18px;font-weight:700}
.phone{position:absolute;left:0;width:1200px;top:92px;font-size:18px;font-weight:700;color:var(--orange)}
.social{position:absolute;left:546px;top:148px;display:flex;gap:14px}
.social span{width:14px;height:14px;border-radius:50%;background:var(--white)}
.copyright{top:4317px;height:52px;background:var(--orange);font-size:10px;display:flex;align-items:center;justify-content:center;color:var(--ink)}
</style>
</head>
<body>

<header class="site-header">
  <div class="abs brand"><span class="brand-dot"></span><span class="brand-name">Marlowe Finch</span></div>
  <div class="abs contact">
    <span><svg width="26" height="26" viewBox="0 0 26 26"><circle cx="13" cy="13" r="12" fill="none" stroke="#f7941d" stroke-width="2"/><path d="M9 7l3 3-2 2c1 2 2 3 4 4l2-2 3 3-2 2c-5 0-10-5-10-10z" fill="#f7941d"/></svg>(555) 014 2298</span>
    <span><svg width="26" height="26" viewBox="0 0 26 26"><circle cx="13" cy="13" r="13" fill="#f7941d"/><rect x="7" y="9" width="12" height="8" fill="#fff"/><path d="M7 9l6 5 6-5" fill="none" stroke="#f7941d" stroke-width="1.4"/></svg>hello@marlowefinch.fit</span>
  </div>
  <nav class="abs main-nav">
    <span class="nav-ring"></span>
    <a class="active" href="#home">Home</a><a href="#about">About Me</a><a href="#services">My Services</a><a href="#events">Events</a><a href="#blog">Blog</a>
  </nav>
</header>

<section class="hero" id="home">
  <div class="photo hero-photo" role="img" aria-label="Athletic woman in sportswear crouching, resting between bodyweight exercises"></div>
  <div class="abs hero-kicker">Start adding</div>
  <h1 class="abs hero-title">Bodyweight<br>Movements</h1>
  <div class="abs hero-sub">into your training &amp; enjoy the results!</div>
  <a class="btn" href="#services">Start training Now !</a>
</section>

<section class="about" id="about">
  <h2 class="abs section-title">About us</h2>
  <p class="abs about-lead">Train smarter, move freely. Strength built from your own body: simple tools, steady progress, real results that last.</p>
  <p class="abs about-text">Every session is planned around you, your goals and your schedule. We work on form first, then build strength, balance and stamina using nothing but bodyweight. No crowded gyms and no complicated machines, just clear coaching, honest feedback and plans you can follow at home, outdoors or in the park.</p>
  <a class="btn" href="#about">Read more</a>
  <div class="photo about-photo" role="img" aria-label="Smiling woman splashing water from a bottle after a workout"></div>
</section>

<section class="band">
  <div class="photo band-photo" role="img" aria-label="Man and woman doing bodyweight squat exercises facing each other"></div>
  <p class="abs band-lead">I am a freelance Personal Trainer based in London specialising in</p>
  <h2 class="abs band-title">Bodyweight Training<br>for Men and Women</h2>
</section>

<section class="services" id="services">
  <h2 class="abs section-title">Our Service</h2>
  <div class="abs service-card" style="left:163px">
    <div class="service-img" role="img" aria-label="Woman stretching on a beach" style="background:linear-gradient(#9fb8cc,#d6dde2 60%,#b9b0a2)"></div>
    <div class="service-name">STRETCHING</div>
    <div class="service-text">Gentle mobility work to ease tight muscles and improve range.</div>
  </div>
  <div class="abs service-card" style="left:460px">
    <div class="service-img" role="img" aria-label="Man doing a bodyweight exercise in a gym" style="background:linear-gradient(135deg,#6f8fae,#c9d5de 55%,#8b99a6)"></div>
    <div class="service-name">BODYWEIGHT EXERCISE</div>
    <div class="service-text">Push, pull and squat patterns built for real strength.</div>
  </div>
  <div class="abs service-card" style="left:757px">
    <div class="service-img" role="img" aria-label="Fitness gear laid out on a floor" style="background:linear-gradient(135deg,#7c7f86,#a9a19a 50%,#5d6470)"></div>
    <div class="service-name">FITNESS PLANS</div>
    <div class="service-text">Weekly plans that fit your life and keep you moving.</div>
  </div>
  <a class="btn" href="#services">More service</a>
</section>

<section class="blog" id="blog">
  <h2 class="abs section-title">Latest Blog</h2>
  <article class="abs post" style="top:146px">
    <div class="post-img" role="img" aria-label="Woman resting after a workout" style="background:linear-gradient(135deg,#3c6c8c,#c69a7e 60%,#2d4b63)"><span class="post-date">22</span></div>
    <div class="post-body"><h3 class="post-title">Why bodyweight training works for everyone</h3><p class="post-text">Bodyweight training scales to any level. Beginners learn clean movement while experienced athletes add tempo, pauses and harder variations. Here is how to start simply and keep progressing week after week without any equipment.</p></div>
  </article>
  <article class="abs post" style="top:312px">
    <div class="post-img" role="img" aria-label="Trainer coaching a client in a gym" style="background:linear-gradient(135deg,#4b4c52,#b98a6d 55%,#2f3034)"><span class="post-date">18</span></div>
    <div class="post-body"><h3 class="post-title">Five moves to build a stronger core</h3><p class="post-text">A strong core protects your back and improves every lift. These five simple movements take ten minutes, need no kit and can be done at home before work. Try them three times a week and notice the change.</p></div>
  </article>
  <article class="abs post" style="top:475px">
    <div class="post-img" role="img" aria-label="Group fitness class exercising together" style="background:linear-gradient(135deg,#5d6b7a,#c7a48c 55%,#3e4a57)"><span class="post-date">12</span></div>
    <div class="post-body"><h3 class="post-title">Training outdoors through the seasons</h3><p class="post-text">Park sessions are great all year round with a little planning. Learn how to warm up properly on cold mornings, stay safe on wet ground and keep your motivation high when the days get shorter.</p></div>
  </article>
  <a class="btn" href="#blog">View all blog posts</a>
</section>

<section class="lower" id="events">
  <h2 class="abs col-title" style="left:96px">Events</h2>
  <div class="abs arrows" style="left:506px"><span><svg width="8" height="10"><path d="M7 1L2 5l5 4" fill="none" stroke="#fff" stroke-width="2"/></svg></span><span><svg width="8" height="10"><path d="M1 1l5 4-5 4" fill="none" stroke="#fff" stroke-width="2"/></svg></span></div>
  <div class="abs rule" style="left:96px;width:460px"></div>
  <div class="abs event" style="top:166px">
    <div class="event-date"><div class="event-day">30</div><div class="event-month">Oct</div></div>
    <div><div class="event-title">Saturday bootcamp in the park</div><div class="event-text">Open group session for all levels,<br>meet at the main gate at nine.</div></div>
  </div>
  <div class="abs event-sep" style="top:258px"></div>
  <div class="abs event" style="top:276px">
    <div class="event-date"><div class="event-day">31</div><div class="event-month">Oct</div></div>
    <div><div class="event-title">Mobility and stretch workshop</div><div class="event-text">Two hours on flexibility, posture<br>and easy recovery routines.</div></div>
  </div>

  <h2 class="abs col-title" style="left:642px">Testimonials</h2>
  <div class="abs arrows" style="left:1060px"><span><svg width="8" height="10"><path d="M7 1L2 5l5 4" fill="none" stroke="#fff" stroke-width="2"/></svg></span><span><svg width="8" height="10"><path d="M1 1l5 4-5 4" fill="none" stroke="#fff" stroke-width="2"/></svg></span></div>
  <div class="abs rule" style="left:642px;width:470px"></div>
  <div class="abs avatar" role="img" aria-label="Portrait of a client"></div>
  <div class="abs avatar-name">Rowena</div>
  <p class="abs quote"><b>“</b> Training with Marlowe changed how I feel every day. Sessions are friendly, focused and always challenging in the right way. I am stronger, my back pain is gone and I finally enjoy exercise. Highly recommended for anyone starting out. <b>”</b></p>
</section>

<footer class="site-footer">
  <div class="address">42 Larkspur Row, Camden, London NW1 8QT</div>
  <div class="phone">Phone (555) 014 2298</div>
  <div class="social"><span></span><span></span><span></span><span></span></div>
</footer>
<div class="abs copyright" style="left:0;width:1200px">© 2017 All rights reserved by Marlowe Finch</div>

</body>
</html>
```